Bold Cover needed for a book on Workplace Bullying

I need a book cover design for a book titled, “Iron Silence?” The book recounts my story of bullying in the workplace. It also includes chapters on how readers can minimize/stop workplace bullying, write an effective complaint, and ensure their own mental wellbeing.
I am looking for a bold design using red and black, and possibly distressed lettering. The covers of other books dealing with this subject do not reflect my vision. They are often too childish or look too academic. This book needs to stress the serious nature of a toxic workplace, while appealing to readers experiencing a similar situation. I’d like the cover to reflect the mental anguish associated with workplace bullying (hence the distressed lettering).
I have included a cover that appeals to me (although the coloring is wrong). That said, I am also very happy (and excited) to see your creative input!
On the cover, it should have the following:
Title: Iron Silence?
Subtitle: How the Harbour Works Department Condones Bullying & Ruins Lives
Author: Owen Frick
Other relevant details:
Book size: 5.5” x 8.5”
Back cover will have a blurb, author picture/short bio, and barcode
The blurb on the back cover reads:
Undermining, intimidation and threats
Despite the Department of Harbour Works allegedly holding a zero tolerance for bullying, these behaviours were an everyday occurrence in at least one workplace. Even after a decade of complaints, numerous witnesses and physical proof, the department failed to act. Instead, they looked the other way, allowing one powerful and well-connected individual to end careers and ruin lives.
After being targeted, one teacher resolved to put an end to the abuse experienced by more than fifty employees. His startling story reveals the relentless bullying, mental health ramifications, and insidious tactics used to cover up the corrosive behaviour.
Those who have experienced a toxic workplace will also find much needed support and guidance, intended to minimise suffering and detail a clear way forward. Chapters include dealing with bullying in the workplace, how to lodge a successful complaint, and how to stay sane during any potential legal action.

```html
<!DOCTYPE html>
<html lang="en">
<head>
<meta charset="utf-8">
<title>Iron Silence? — Owen Frick</title>
<link rel="stylesheet" href="https://fonts.googleapis.com/css2?family=Bebas+Neue&family=Rubik+Dirt&display=swap">
<style>
  :root {
    --cover-red: #e31e25;
    --crack-red: #6e070a;
    --crack-dark: #3a0305;
    --title-ink: #2b2a28;
    --paper-white: #ffffff;
  }
  html, body {
    margin: 0;
    padding: 0;
    width: 796px;
    height: 1200px;
    overflow: hidden;
    background: var(--cover-red);
  }
  .cover {
    position: relative;
    width: 796px;
    height: 1200px;
    background: var(--cover-red);
    overflow: hidden;
  }
  .crack-texture {
    position: absolute;
    left: 0;
    top: 300px;
    width: 640px;
    height: 900px;
  }
  .title {
    position: absolute;
    left: 0;
    top: 104px;
    width: 796px;
    margin: 0;
    text-align: center;
    font-family: "Rubik Dirt", "Impact", sans-serif;
    font-weight: 400;
    font-size: 168px;
    line-height: 145px;
    letter-spacing: -4px;
    color: var(--title-ink);
    text-transform: uppercase;
    transform-origin: 50% 50%;
    transform: skewX(-9deg) scaleX(0.74);
    white-space: nowrap;
  }
  .title-line { display: block; }
  .subtitle {
    position: absolute;
    right: 101px;
    top: 405px;
    margin: 0;
    text-align: right;
    font-family: "Bebas Neue", "Arial Narrow", sans-serif;
    font-weight: 400;
    font-size: 26px;
    line-height: 27px;
    color: var(--paper-white);
    text-transform: uppercase;
  }
  .author {
    position: absolute;
    right: 101px;
    top: 1008px;
    margin: 0;
    font-family: "Bebas Neue", "Arial Narrow", sans-serif;
    font-weight: 400;
    font-size: 44px;
    line-height: 44px;
    color: var(--paper-white);
    text-transform: uppercase;
  }
</style>
</head>
<body>
  <main class="cover">
    <svg class="crack-texture" viewBox="0 0 640 900" role="img" aria-label="Dark cracks spreading across a red surface, from the title down to the bottom edge">
      <defs>
        <radialGradient id="crackCore" cx="0.5" cy="0.5" r="0.5">
          <stop offset="0" stop-color="var(--crack-dark)" stop-opacity="0.55"/>
          <stop offset="0.5" stop-color="var(--crack-red)" stop-opacity="0.25"/>
          <stop offset="1" stop-color="var(--crack-red)" stop-opacity="0"/>
        </radialGradient>
        <radialGradient id="crackHaze" cx="0.5" cy="0.5" r="0.5">
          <stop offset="0" stop-color="var(--crack-red)" stop-opacity="0.35"/>
          <stop offset="1" stop-color="var(--crack-red)" stop-opacity="0"/>
        </radialGradient>
      </defs>
      <ellipse cx="110" cy="260" rx="120" ry="260" fill="url(#crackHaze)"/>
      <ellipse cx="260" cy="420" rx="250" ry="140" fill="url(#crackHaze)"/>
      <ellipse cx="230" cy="620" rx="90" ry="200" fill="url(#crackHaze)"/>
      <ellipse cx="300" cy="740" rx="260" ry="120" fill="url(#crackCore)"/>
      <ellipse cx="500" cy="760" rx="110" ry="110" fill="url(#crackHaze)"/>
    </svg>

    <h1 class="title">
      <span class="title-line">Iron</span>
      <span class="title-line">Silence?</span>
    </h1>

    <p class="subtitle">How the Harbour Works Department<br>Condones Bullying &amp; Ruins Lives</p>

    <p class="author">Owen Frick</p>
  </main>
</body>
</html>
```